Bright Kettle Crafts- Retailer

Need to describe what Bright Kettle Crafts is, what products we carry with photos and descriptions, as well as pricing for each. shopping cart, purchase items by way of Paloo and CoinDrift

Industry/Entity Type

Hobby / Entertainment

Coding

Coded - Design and coding required

Number of Pages Required

5+ page

Font styles to use
Sans Serif

Colors
0054AA
0677BA
7BADD7
CADEEF
E8F1F8
F0912C
F2A743
F7CA91
FBE8D2
FDF5EE
EE7325
F08F49
F5BC92
FAE3D3
FDF4ED

Requirements
Must have
• Product pages, shopping cart, checkout
Nice to have
• Video/gif, of working train or slot car tracks
Should not have
• Cartoon characters or images

```html
<!DOCTYPE html>
<html lang="en">
<head>
<meta charset="utf-8">
<title>Bright Kettle Crafts — Shop</title>
<link rel="stylesheet" href="https://fonts.googleapis.com/css2?family=IBM+Plex+Mono:wght@400;500&family=IBM+Plex+Sans:wght@400;600&display=swap">
<style>
  :root {
    --blue-deep: #0054AA;
    --blue-mid: #0677BA;
    --blue-soft: #CADEEF;
    --blue-mist: #E8F1F8;
    --orange: #EE7325;
    --ink: #1c1f24;
    --ink-muted: #5d6166;
    --ink-faint: #8a8f95;
    --paper: #ffffff;
  }
  * { box-sizing: border-box; margin: 0; padding: 0; }
  html, body {
    width: 1200px;
    height: 1089px;
    overflow: hidden;
    background: var(--paper);
  }
  body {
    font-family: "IBM Plex Sans", sans-serif;
    color: var(--ink);
  }
  .product-grid {
    display: grid;
    grid-template-columns: 560px 560px;
    column-gap: 43px;
    row-gap: 45px;
    padding: 87px 0 0 20px;
  }
  .product-card {
    border: 1.5px solid var(--blue-soft);
    border-radius: 4px;
    background: var(--paper);
    overflow: hidden;
    min-height: 620px;
  }
  .product-media {
    position: relative;
    height: 246px;
    background: var(--blue-mist);
  }
  .scale-badge {
    position: absolute;
    top: 19px;
    left: 18px;
    padding: 8px 14px;
    background: var(--blue-deep);
    color: var(--paper);
    font-family: "IBM Plex Mono", monospace;
    font-size: 17px;
    line-height: 22px;
    border-radius: 2px;
  }
  .product-body {
    padding: 36px 36px 35px;
  }
  .product-sku {
    font-family: "IBM Plex Mono", monospace;
    font-size: 17px;
    line-height: 22px;
    color: var(--ink-faint);
    letter-spacing: 0.02em;
  }
  .product-name {
    margin-top: 29px;
    font-size: 26px;
    line-height: 34px;
    font-weight: 600;
  }
  .product-description {
    margin-top: 22px;
    font-size: 21px;
    line-height: 37px;
    color: var(--ink-muted);
  }
  .product-footer {
    margin-top: 32px;
    display: flex;
    justify-content: space-between;
    align-items: center;
  }
  .product-price {
    font-family: "IBM Plex Mono", monospace;
    font-size: 28px;
    font-weight: 500;
    color: var(--blue-deep);
  }
  .add-to-cart {
    width: 90px;
    height: 56px;
    border: 1.5px solid var(--orange);
    border-radius: 2px;
    background: var(--paper);
    color: var(--orange);
    font-family: "IBM Plex Mono", monospace;
    font-size: 17px;
    letter-spacing: 0.04em;
  }
</style>
</head>
<body>
  <main class="product-grid">
    <article class="product-card">
      <div class="product-media" role="img" aria-label="Line drawing of a steam locomotive">
        <span class="scale-badge">HO 1:87</span>
      </div>
      <div class="product-body">
        <p class="product-sku">SKU HO-2882</p>
        <h2 class="product-name">Northbound 2-8-2 Mikado</h2>
        <p class="product-description">Die-cast steam locomotive with directional headlamp and metal driver rods.</p>
        <div class="product-footer">
          <span class="product-price">$289.00</span>
          <button class="add-to-cart" type="button">ADD</button>
        </div>
      </div>
    </article>

    <article class="product-card">
      <div class="product-media" role="img" aria-label="Line drawing of a diesel switcher">
        <span class="scale-badge">N 1:160</span>
      </div>
      <div class="product-body">
        <p class="product-sku">SKU NS-100</p>
        <h2 class="product-name">Tabletop branch line starter set</h2>
        <p class="product-description">Diesel switcher, two freight cars, 36 in. of curved track, and a power pack.</p>
        <div class="product-footer">
          <span class="product-price">$149.00</span>
          <button class="add-to-cart" type="button">ADD</button>
        </div>
      </div>
    </article>

    <article class="product-card">
      <div class="product-media" role="img" aria-label="Line drawing of a slot car">
        <span class="scale-badge">1:32</span>
      </div>
      <div class="product-body">
        <p class="product-sku">SKU SC-1232</p>
        <h2 class="product-name">Slot car circuit — 12 ft. oval</h2>
      </div>
    </article>

    <article class="product-card">
      <div class="product-media" role="img" aria-label="Line drawing of a pine tree">
        <span class="scale-badge">ANY SCALE</span>
      </div>
      <div class="product-body">
        <p class="product-sku">SKU SCN-04</p>
        <h2 class="product-name">Trackside scenery pack</h2>
      </div>
    </article>
  </main>
</body>
</html>
```